The Calm of Orchards New Book Cover Design Project

Book cover design . Paperback, ebook, and Vocara (derived from book cover) files/images required.
Book Title: The Calm of Orchards
Subtitle: Fewer Rusty Gates
Author: Dorian Halvey
Files: Ebook, Paperback (Brellix & Tolvent Press), Vocara sized image
File size & information to be provided once design is ready. Brellix paperback will be 5.25 x 8.
Completion date is flexible. Planning to publish in November.
Updates

Need extra days to review

Target Market(s)

Motorcycle owners

Font styles to use
Sans Serif

Requirements
Must have
• A generic looking motorcycle (samples attached). Thumbnail easily recognized as a motorcycle book.
Nice to have
• Open to all ideas but am favoring my idea: to emphasize the title lettering similar to (but not a copy of) other Calm books (examples attached), on a plain background. All books in the category have a motorcycle on the cover. Author name and subtitle do not have to be prominent. Rider optional..
Should not have
• Should not look like a biker romance or fantasy cover or look cartoonish. Motorcycle pic should be fairly generic (brand, style,).

```html
<!DOCTYPE html>
<html lang="en">
<head>
<meta charset="utf-8">
<title>The Calm of Orchards — Dorian Halvey</title>
<link rel="stylesheet" href="https://fonts.googleapis.com/css2?family=Bodoni+Moda:opsz,wght@6..96,400;6..96,500;6..96,600&display=swap">
<style>
  :root {
    --paper: #ffffff;
    --ink: #0b0b0b;
    --title-red: #f70000;
    --bike-dark: #15192a;
    --bike-mid: #3a4260;
    --bike-light: #9aa0ad;
  }
  html, body {
    margin: 0;
    padding: 0;
    width: 800px;
    height: 1200px;
    overflow: hidden;
    background: var(--paper);
  }
  .cover {
    position: relative;
    width: 800px;
    height: 1200px;
    background: var(--paper);
    font-family: "Bodoni Moda", "Didot", serif;
    color: var(--ink);
  }
  .cover > * {
    position: absolute;
    left: 0;
    width: 800px;
    margin: 0;
    text-align: center;
    line-height: 1;
  }
  .title-the {
    top: 82px;
    font-size: 78px;
    font-weight: 500;
    letter-spacing: 0.01em;
    z-index: 2;
  }
  .title-key {
    top: 128px;
    font-size: 330px;
    font-weight: 400;
    color: var(--title-red);
    letter-spacing: -0.02em;
    z-index: 1;
  }
  .title-of {
    top: 392px;
    font-size: 78px;
    font-weight: 500;
    z-index: 2;
  }
  .title-subject {
    top: 448px;
    font-size: 132px;
    font-weight: 500;
    letter-spacing: -0.005em;
  }
  .subtitle {
    top: 636px;
    font-size: 24px;
    font-weight: 500;
    letter-spacing: 0.6em;
    text-indent: 0.6em;
    text-transform: uppercase;
  }
  .motorcycle-photo {
    top: 712px;
    left: 188px;
    width: 532px;
    height: 336px;
    border-radius: 46% 40% 44% 48% / 52% 46% 50% 48%;
    background:
      radial-gradient(ellipse at 30% 70%, var(--bike-dark) 0%, transparent 45%),
      radial-gradient(ellipse at 65% 35%, var(--bike-mid) 0%, transparent 55%),
      radial-gradient(ellipse at 55% 60%, var(--bike-light) 0%, transparent 70%);
    opacity: 0.9;
  }
  .author {
    top: 1090px;
    font-size: 40px;
    font-weight: 500;
    letter-spacing: 0.72em;
    text-indent: 0.72em;
    text-transform: uppercase;
  }
</style>
</head>
<body>
  <main class="cover">
    <h1 class="book-title">
      <span class="title-the" style="position:absolute;left:0;width:800px;">The</span>
      <span class="title-key" style="position:absolute;left:0;width:800px;">Calm</span>
      <span class="title-of" style="position:absolute;left:0;width:800px;">of</span>
      <span class="title-subject" style="position:absolute;left:0;width:800px;">Orchards</span>
    </h1>
    <p class="subtitle">Fewer Rusty Gates</p>
    <div class="motorcycle-photo" role="img" aria-label="Photograph of a dark blue café racer motorcycle with chrome wheels and exhaust, seen from the rear three-quarter view"></div>
    <p class="author">Dorian Halvey</p>
  </main>
</body>
</html>
```